Personal training and nutrition business needs business card design

We need a business card that outlays our services and invites potential customers to join our team and take the first step to a healthier and more enjoyable life. We cater for any level of fitness and specialize in weight loss and conditioning, strength training, muscle gain and strength endurance. Whether you are just starting off or need some help getting to the next level of your journey we are here to get the job done.
We specialize in one on one or one on two personal training sessions and each program will be custom made to suit individual fitness goals of our clients

```html
<!DOCTYPE html>
<html lang="en">
<head>
<meta charset="utf-8">
<title>Stride &amp; Tempo – Business Card</title>
<link href="https://fonts.googleapis.com/css2?family=Michroma&family=Roboto:wght@400;500&display=swap" rel="stylesheet">
<style>
  :root {
    --stage: #2b2b2d;
    --card-black: #0a0a0a;
    --purple: #7a4aa8;
    --purple-deep: #52307a;
    --purple-bright: #b070d0;
    --pink: #e070e8;
    --white: #ffffff;
    --divider: #2a2a2a;
  }
  * { box-sizing: border-box; margin: 0; padding: 0; }
  html, body { width: 1200px; height: 1015px; overflow: hidden; }
  body {
    background: var(--stage);
    position: relative;
    font-family: "Roboto", Arial, sans-serif;
  }
  .card {
    position: absolute;
    width: 640px;
    height: 366px;
    box-shadow: 0 18px 40px rgba(0,0,0,.55);
  }

  /* Front: purple pattern side */
  .card-front { left: 110px; top: 80px; overflow: hidden; }
  .pattern-field {
    position: absolute; inset: 0;
    background: linear-gradient(160deg, var(--pink) 0%, var(--purple) 45%, var(--purple-deep) 100%);
  }
  .front-brand {
    position: absolute; left: 330px; top: 160px;
    display: flex; align-items: center; gap: 12px;
    font-family: "Michroma", sans-serif;
    color: var(--white);
    font-size: 24px; line-height: 1.1;
  }
  .brand-dot {
    width: 22px; height: 22px; border-radius: 50%;
    background: var(--white); flex: none;
  }

  /* Back: black info side */
  .card-back {
    left: 450px; top: 560px;
    background: var(--card-black);
  }
  .back-divider {
    position: absolute; left: 300px; top: 40px; bottom: 90px;
    width: 1px; background: var(--divider);
  }
  .back-brand {
    position: absolute; left: 40px; top: 90px; width: 240px;
    text-align: left;
  }
  .back-brand .brand-row {
    display: flex; align-items: center; gap: 12px;
    font-family: "Michroma", sans-serif;
    color: var(--white);
    font-size: 26px; line-height: 1.15;
  }
  .back-brand .brand-dot { background: var(--purple-bright); width: 26px; height: 26px; }
  .services {
    margin-top: 10px;
    font-family: "Roboto", sans-serif;
    font-size: 8.5px; letter-spacing: .8px;
    color: var(--purple-bright); text-transform: uppercase;
  }
  .contact {
    position: absolute; left: 330px; top: 60px;
    color: var(--white);
  }
  .person-name {
    font-size: 20px; font-weight: 500; letter-spacing: .5px;
    color: var(--purple-bright); text-transform: uppercase;
  }
  .person-role { font-size: 15px; margin-bottom: 12px; }
  .contact-list { list-style: none; font-size: 15px; line-height: 1.45; }
  .contact-list li { display: flex; align-items: center; gap: 8px; }
  .contact-list svg { width: 14px; height: 14px; flex: none; }
  .accent { color: var(--purple-bright); }
  .address { margin-top: 12px; font-size: 15px; line-height: 1.35; padding-left: 22px; }
  .motto {
    position: absolute; left: 0; right: 0; bottom: 34px;
    text-align: center;
    font-family: "Michroma", sans-serif;
    font-size: 22px; letter-spacing: 1px;
    color: var(--purple-bright);
  }
</style>
</head>
<body>

  <section class="card card-front">
    <div class="pattern-field" role="img" aria-label="Repeating brand pattern in pink and purple tones"></div>
    <div class="front-brand">
      <span class="brand-dot"></span>
      <span>STRIDE<br>&amp; TEMPO</span>
    </div>
  </section>

  <section class="card card-back">
    <div class="back-brand">
      <div class="brand-row">
        <span class="brand-dot"></span>
        <span>STRIDE<br>&amp; TEMPO</span>
      </div>
      <p class="services">Personal training. Nutrition. Motivation</p>
    </div>

    <div class="back-divider"></div>

    <div class="contact">
      <p class="person-name">Daniel Reyes</p>
      <p class="person-role">Managing Director</p>
      <ul class="contact-list">
        <li>
          <svg viewBox="0 0 24 24" fill="none" stroke="#b070d0" stroke-width="2.4"><path d="M5 3h4l2 5-3 2a12 12 0 0 0 6 6l2-3 5 2v4a2 2 0 0 1-2 2A17 17 0 0 1 3 5a2 2 0 0 1 2-2z"/></svg>
          055-210 384 672
        </li>
        <li>
          <svg viewBox="0 0 24 24" fill="none" stroke="#b070d0" stroke-width="2.4"><rect x="3" y="5" width="18" height="14" rx="1"/><path d="M3 6l9 7 9-7"/></svg>
          hello@stridetempo.com
        </li>
        <li>
          <svg viewBox="0 0 24 24" fill="none" stroke="#b070d0" stroke-width="2"><circle cx="12" cy="12" r="9"/><path d="M3 12h18M12 3c3 3 3 15 0 18M12 3c-3 3-3 15 0 18"/></svg>
          <span>www.<span class="accent">stridetempo</span>.com</span>
        </li>
      </ul>
      <p class="address">88, Harbour Road East<br>30917, Countryland</p>
    </div>

    <p class="motto">COMMIT. PREFORM. SUCCEED</p>
  </section>

</body>
</html>
```